Harbor Nightclub

Nightclub flyer., digital single sided, for KV and PX. I included samples of some previous flyers we've used. Sample Info:
HARBOR
FRIDAYS
FRI MAY 1 2020
DJ VORTAN (club floor)
DJ RUZO & DJ TAV (residents on the lounge floor)
4217 Marlow Avenue Sacramento
www.harborvenuehall.example for list/VIP inquiries

Target Market(s)

Upscale top 40 crowd but want some cool and artsy like the examples included.

Font styles to use
Sans Serif

Requirements
Must have
• Harbor Logo
Nice to have
• Would be nice if the flyer can be incorporated later with DJ photos (sometimes we will add dj photos to pixagram etc). Would like a big city type of feel.
Should not have
• Nothing too sexual.

```html
<!DOCTYPE html>
<html lang="en">
<head>
<meta charset="utf-8">
<title>Harbor Nightclub – Fridays</title>
<link rel="stylesheet" href="https://fonts.googleapis.com/css2?family=Antonio:wght@700&family=Questrial&display=swap">
<style>
  :root {
    --backdrop: #000000;
    --flyer-edge: #8a8a8a;
    --night-deep: #0d0812;
    --night-violet: #3a1c4e;
    --city-blue: #1f2f5c;
    --city-glow: #6b3a7a;
    --ember: #8a4a4a;
    --neon: #ff3df0;
    --headline: #ffffff;
    --dj-grey: #c9c5cc;
    --body-text: #f2eef5;
    --badge-box: #1c0f2b;
  }
  * { margin: 0; padding: 0; box-sizing: border-box; }
  html, body {
    width: 1200px; height: 1200px; overflow: hidden;
    background: var(--backdrop);
  }
  .flyer {
    position: absolute; left: 171px; top: 54px;
    width: 840px; height: 1063px;
    border: 1px solid var(--flyer-edge);
    overflow: hidden;
    background: var(--night-deep);
  }
  .city-scene {
    position: absolute; inset: 0;
    background:
      radial-gradient(ellipse 45% 25% at 80% 35%, rgba(138,74,74,.55), transparent 70%),
      radial-gradient(ellipse 60% 35% at 45% 30%, rgba(107,58,122,.75), transparent 70%),
      radial-gradient(ellipse 50% 40% at 15% 45%, rgba(31,47,92,.8), transparent 70%),
      linear-gradient(180deg, #07050b 0%, #1a1028 14%, var(--night-violet) 28%, #2a1a40 50%, #1b1230 68%, #150c20 82%, #1e0c2a 100%);
  }
  .bottom-fade {
    position: absolute; left: 0; right: 0; bottom: 0; height: 340px;
    background: linear-gradient(180deg, transparent 0%, rgba(20,8,28,.75) 45%, rgba(36,14,48,.95) 100%);
  }
  .neon-frame { position: absolute; inset: 0; }
  .headline {
    position: absolute; left: 240px; top: 618px; width: 350px;
    text-align: center;
    font-family: "Antonio", "Arial Narrow", sans-serif;
    font-weight: 700; font-size: 196px; line-height: 1;
    color: var(--headline);
    transform: scaleX(0.72);
    letter-spacing: -2px;
  }
  .lineup {
    position: absolute; left: 58px; top: 818px; width: 800px;
    white-space: nowrap; color: var(--dj-grey);
  }
  .dj {
    font-family: "Antonio", "Arial Narrow", sans-serif;
    font-weight: 700; font-size: 50px; line-height: 1;
    display: inline-block; transform: scaleX(0.72); transform-origin: left;
    margin-right: -40px;
  }
  .dj.pair { margin-right: -50px; }
  .floor {
    font-family: "Questrial", sans-serif; font-size: 19px;
    vertical-align: 2px; margin-right: 6px;
  }
  .venue-info {
    position: absolute; left: 0; width: 840px; top: 888px;
    text-align: center;
    font-family: "Questrial", sans-serif; font-size: 20px; line-height: 25px;
    color: var(--body-text);
  }
  .date {
    position: absolute; left: 158px; top: 970px;
    font-family: "Questrial", sans-serif; font-size: 31px;
    color: var(--body-text); letter-spacing: 1px;
  }
  .brand-badge {
    position: absolute; left: 475px; top: 936px;
    width: 254px; height: 98px;
    background: var(--badge-box);
    display: flex; align-items: center; gap: 20px; padding-left: 14px;
  }
  .brand-dot {
    width: 56px; height: 56px; border-radius: 50%;
    border: 3px solid var(--body-text);
  }
  .brand-name {
    font-family: "Questrial", sans-serif; font-size: 30px;
    color: var(--body-text); letter-spacing: 1px;
  }
</style>
</head>
<body>
  <main class="flyer">
    <div class="city-scene" role="img" aria-label="Night-time aerial photo of a dense city of lit high-rise towers in violet and blue haze"></div>
    <div class="bottom-fade"></div>

    <svg class="neon-frame" width="840" height="1063" viewBox="0 0 840 1063" aria-hidden="true">
      <defs>
        <filter id="neon-glow" x="-20%" y="-20%" width="140%" height="140%">
          <feGaussianBlur stdDeviation="7" result="blur"/>
          <feMerge><feMergeNode in="blur"/><feMergeNode in="blur"/><feMergeNode in="SourceGraphic"/></feMerge>
        </filter>
      </defs>
      <polyline points="380,234 261,196 118,372 645,614 705,338 437,252"
                fill="none" stroke="var(--neon)" stroke-width="3.5" filter="url(#neon-glow)"/>
    </svg>

    <h1 class="headline">FRIDAYS</h1>

    <p class="lineup">
      <span class="dj">DJ VORTAN</span><span class="floor">(club floor)</span>
      <span class="dj pair">DJ RUZO &amp; DJ TAV</span><span class="floor">(residents on the lounge floor)</span>
    </p>

    <p class="venue-info">4217 Marlow Avenue Sacramento<br>www.harborvenuehall.example for list/VIP inquiries</p>

    <p class="date">FRIDAY &bull; MAY 1 2020</p>

    <div class="brand-badge">
      <span class="brand-dot"></span>
      <span class="brand-name">HARBOR</span>
    </div>
  </main>
</body>
</html>
```